Label Design for Saffron Company

We need a label design that is unique for our container. The item inside the container is Saffron, and it is 5g in weigh. We need on the label our logo, the weight and quality. Here is the exactly what we want. We want the background to be black for the label and the design to present royalty, and premium quality.

Premium Quality
Grade A+ Premium Saffron
100% Natural and Pure
www.VelmoraSpice.com

Target Market(s)

Everyone

Requirements
Must have
• Black background, golden border design. Unique design, that show premium and royalty.
Nice to have
• The logo is attached with transparent background so you can show exactly how things look like.
Should not have
• different colors that are not part of the logo.

```html
<!DOCTYPE html>
<html lang="en">
<head>
<meta charset="utf-8">
<title>Velmora Spice – Saffron Lid Labels</title>
<link rel="stylesheet" href="https://fonts.googleapis.com/css2?family=Cinzel:wght@400&family=Montserrat:wght@500;600;700&display=swap">
<style>
  :root {
    --backdrop: #c3c3c3;
    --label-black: #0b0b0c;
    --label-black-soft: #151516;
    --gold: #d9b95f;
    --gold-line: #c9a64a;
    --ivory: #f2efe8;
  }
  html, body {
    margin: 0;
    padding: 0;
    width: 1200px;
    height: 2664px;
    overflow: hidden;
    background: var(--backdrop);
  }
  .label-sheet { display: block; width: 1200px; height: 2664px; }
  .label-disc { fill: url(#discTone); }
  .border-ring { fill: none; stroke: var(--gold-line); stroke-width: 0.45; }
  .arc-text {
    font-family: "Montserrat", sans-serif;
    font-weight: 500;
    font-size: 5.2px;
    letter-spacing: 1.6px;
    fill: var(--ivory);
  }
  .brand-square { fill: none; stroke: var(--gold-line); stroke-width: 0.9; }
  .brand-top, .brand-main {
    font-family: "Cinzel", serif;
    font-weight: 400;
    fill: var(--ivory);
    text-anchor: middle;
  }
  .brand-top { font-size: 9.4px; letter-spacing: 1.6px; }
  .brand-main { font-size: 14.5px; letter-spacing: 0.4px; }
  .grade {
    font-family: "Montserrat", sans-serif;
    font-weight: 700;
    font-size: 5.8px;
    letter-spacing: 1.8px;
    fill: var(--ivory);
    text-anchor: middle;
  }
  .product-name {
    font-family: "Montserrat", sans-serif;
    font-weight: 700;
    font-size: 15px;
    fill: var(--gold);
    text-anchor: middle;
  }
  .purity {
    font-family: "Montserrat", sans-serif;
    font-weight: 500;
    font-size: 5.3px;
    fill: var(--ivory);
    text-anchor: middle;
  }
  .net-weight {
    font-family: "Montserrat", sans-serif;
    font-weight: 600;
    font-size: 10.5px;
    fill: var(--gold);
    text-anchor: middle;
  }
</style>
</head>
<body>
<svg class="label-sheet" viewBox="0 0 1200 2664" xmlns="http://www.w3.org/2000/svg" xmlns:xlink="http://www.w3.org/1999/xlink">
  <defs>
    <radialGradient id="discTone" cx="50%" cy="45%" r="60%">
      <stop offset="0" stop-color="var(--label-black-soft)"/>
      <stop offset="1" stop-color="var(--label-black)"/>
    </radialGradient>
    <filter id="liftShadow" x="-20%" y="-20%" width="140%" height="140%">
      <feDropShadow dx="0" dy="1.2" stdDeviation="1.4" flood-color="#000" flood-opacity="0.35"/>
    </filter>
    <path id="topArc" d="M -81 0 A 81 81 0 0 1 81 0"/>
    <path id="bottomArc" d="M -88 0 A 88 88 0 0 0 88 0"/>

    <g id="labelFace">
      <circle class="label-disc" r="100" filter="url(#liftShadow)"/>
      <path class="border-ring" d="M44,-76.2 A88,88 0 0 1 49.2,73"/>
      <path class="border-ring" d="M-49.2,73 A88,88 0 0 1 -44,-76.2"/>
      <text class="arc-text"><textPath href="#topArc" startOffset="50%" text-anchor="middle">PREMIUM QUALITY</textPath></text>
      <text class="arc-text" dy="5"><textPath href="#bottomArc" startOffset="50%" text-anchor="middle">WWW.VELMORASPICE.COM</textPath></text>

      <rect class="brand-square" x="-13" y="-66" width="26" height="26" rx="3"/>
      <text class="brand-top" y="-23">VELMORA</text>
      <text class="brand-main" y="-7">SPICE</text>

      <text class="grade" y="16">GRADE A+</text>
      <text class="product-name" y="32" textLength="136" lengthAdjust="spacingAndGlyphs">PREMIUM SAFFRON</text>
      <text class="purity" y="42" textLength="110" lengthAdjust="spacing">100% NATURAL AND PURE</text>
    </g>
  </defs>

  <g class="label label-1g" transform="translate(590 301) scale(2.16)">
    <use href="#labelFace"/>
    <text class="net-weight" y="74">1g</text>
  </g>

  <g class="label label-2g" transform="translate(590 804) scale(2.43)">
    <use href="#labelFace"/>
    <text class="net-weight" y="74">2g</text>
  </g>

  <g class="label label-5g" transform="translate(590 1398) scale(3.03)">
    <use href="#labelFace"/>
    <text class="net-weight" y="74">5g</text>
  </g>

  <g class="label label-10g" transform="translate(590 2182) scale(4.09)">
    <use href="#labelFace"/>
    <text class="net-weight" y="74">10g</text>
  </g>
</svg>
</body>
</html>
```